Lantern Walk! A website showcasing who I am as a person

Lantern Walk started out as idea for me to better myself as a person and work on small projects that would help me grow as a person. Now I want to build a website showcasing "Lantern Walk." I want the website to showcase who I am and how I have grown both professionally and personally. I can build the raw code of the website on my own but I am not really much of a designer. I am looking for a design where I can write and post blogs, articles and share my thoughts. A little about myself and the ideas and interests that I want to share
What is Lantern Walk
Who I am
Background - Professional
Brand Marketing
Email Automation
Hiking
Rock Climbing
Traveling
Exercising and Transformation
"Personal Thoughts"
Hopefully this is enough information to get people started on some designs.
Industry/Entity Type
Work
Number of Pages Required
3 page

```html
<!DOCTYPE html>
<html lang="en">
<head>
<meta charset="utf-8">
<title>Lantern Walk</title>
<link rel="stylesheet" href="https://fonts.googleapis.com/css2?family=Montserrat:wght@400;600;700&family=Open+Sans:wght@400;600&family=Poppins:wght@300;400;500&display=swap">
<style>
:root{
  --accent:#4dc3ea;
  --ink:#1f1f1f;
  --text:#6b625c;
  --muted:#8a8a8a;
  --light:#f4f4f4;
  --field:#f3f3f3;
  --track:#eeeeee;
  --dark:#161616;
  --white:#ffffff;
}
*{box-sizing:border-box;margin:0;padding:0}
html,body{width:1200px;height:4018px;overflow:hidden;background:var(--white)}
body{position:relative;font-family:'Poppins',sans-serif;color:var(--text)}
section,header,footer{position:absolute;left:0;width:1200px}
.abs{position:absolute}
.section-title{position:absolute;left:0;width:1200px;text-align:center;font-family:'Montserrat',sans-serif;font-weight:700;font-size:42px;color:var(--ink);letter-spacing:.5px}

/* hero */
.hero{top:0;height:568px;background:linear-gradient(180deg,#9a9a9a 0,#6f6f6f 110px,#4a4a4a 300px,#333 568px);overflow:hidden}
.hero-photo{position:absolute;left:640px;top:0;width:560px;height:568px;background:radial-gradient(ellipse at 55% 45%,#cfcfcf 0,#8d8d8d 30%,#3a3a3a 60%,#1e1e1e 100%)}
.brand{position:absolute;left:54px;top:24px;font-family:'Open Sans',sans-serif;font-weight:600;font-size:34px;color:var(--white);letter-spacing:1px}
.nav{position:absolute;left:643px;top:35px;width:536px;height:35px;background:#000;display:flex;justify-content:space-around;align-items:center;padding:0 14px}
.nav a{font-family:'Open Sans',sans-serif;font-size:15px;color:var(--white);text-decoration:none;letter-spacing:.5px}
.hero-hello{position:absolute;left:59px;top:276px;font-family:'Open Sans',sans-serif;font-size:28px;color:var(--white)}
.hero-role{position:absolute;left:59px;top:314px;font-family:'Open Sans',sans-serif;font-weight:600;font-size:41px;color:var(--white)}
.btn{display:block;background:var(--accent);color:var(--white);font-family:'Montserrat',sans-serif;font-weight:600;text-align:center;text-decoration:none}
.hero-btn{position:absolute;left:59px;top:388px;width:139px;height:35px;line-height:35px;font-size:13px;border-radius:3px}

/* about */
.about{top:568px;height:812px}
.about-text{position:absolute;left:166px;top:126px;width:868px;text-align:center;font-size:16.5px;line-height:36px;color:var(--text);font-weight:300;letter-spacing:.3px}
.skill{position:absolute;left:292px;width:668px;height:20px}
.skill-label{position:absolute;left:0;top:0;font-family:'Montserrat',sans-serif;font-weight:700;font-size:11.5px;letter-spacing:1px;color:#333;line-height:20px}
.skill-track{position:absolute;left:230px;top:5px;width:437px;height:10px;background:var(--track);border-radius:5px}
.skill-fill{height:10px;background:var(--accent);border-radius:5px}

/* works */
.works{top:1380px;height:844px;background:var(--light)}
.filters{position:absolute;top:130px;left:0;width:1200px;display:flex;justify-content:center;gap:26px;font-size:12.5px;color:#555;letter-spacing:.5px}
.filters span.active{color:#222;border-bottom:2px solid #222;padding-bottom:6px}
.work-tile{position:absolute;width:343px;height:276px}

/* blogs */
.blogs{top:2224px;height:562px}
.post{position:absolute;top:104px;width:348px;text-align:center}
.post-image{width:348px;height:196px}
.post-title{margin-top:20px;font-family:'Montserrat',sans-serif;font-weight:700;font-size:13px;letter-spacing:.8px;color:#222}
.post-text{margin-top:8px;font-size:14.5px;line-height:31px;color:var(--text);padding:0 26px}
.post-btn{margin:22px auto 0;width:130px;height:48px;line-height:48px;border-radius:24px;font-size:13px}

/* freelance */
.freelance{top:2786px;height:445px;background:linear-gradient(100deg,#222 0,#111 40%,#2a2a2a 75%,#1a1a1a 100%)}
.freelance-scene{position:absolute;left:0;top:0;width:1200px;height:445px;background:radial-gradient(ellipse at 22% 45%,rgba(90,90,90,.35) 0,rgba(0,0,0,0) 45%)}
.freelance-circle{position:absolute;left:485px;top:75px;width:236px;height:236px;border-radius:50%;background:var(--white);display:flex;align-items:center;justify-content:center;text-align:center;font-family:'Montserrat',sans-serif;font-weight:600;font-size:19px;line-height:26px;color:#111}
.freelance-mail{position:absolute;top:336px;left:0;width:1200px;text-align:center;font-family:'Montserrat',sans-serif;font-size:16px;color:var(--white)}

/* contact */
.contact{top:3231px;height:635px}
.field{position:absolute;left:217px;width:718px;background:var(--field);font-size:14px;color:#a8a8a8;padding:0 10px}
.field-line{height:43px;line-height:43px}
.field-area{height:137px;padding-top:10px}
.submit{position:absolute;left:512px;top:525px;width:128px;height:48px;line-height:48px;border-radius:24px;font-size:12.5px}

/* footer */
.footer{top:3866px;height:152px;background:var(--dark);text-align:center;line-height:152px;font-family:'Montserrat',sans-serif;font-size:15px;color:var(--white)}
</style>
</head>
<body>

<header class="hero">
  <div class="hero-photo" role="img" aria-label="Black and white portrait photo of the site owner wearing glasses and a striped sweater"></div>
  <div class="brand">LANTERN WALK</div>
  <nav class="nav">
    <a href="#">HOME</a><a href="#">ABOUT</a><a href="#">WORK</a><a href="#">BLOG</a><a href="#">CONTACT</a>
  </nav>
  <p class="hero-hello">Hello, I'm Sam Hollis</p>
  <h1 class="hero-role">Web Designer &amp; Developer!</h1>
  <a class="btn hero-btn" href="#">See My Work</a>
</header>

<section class="about">
  <h2 class="section-title" style="top:48px">Everything About Me!</h2>
  <p class="about-text">Lorem Ipsum is simply dummy text of the printing and typesetting industry. Lorem Ipsum has been the industry's standard dummy text ever since the 1500s, when an unknown printer took a galley of type and scrambled it to make a type specimen book. It has survived not only five centuries, but also the leap into electronic typesetting, remaining standard dummy text ever since the 1500s, when an unknown printer took a galley of type and scrambled it to make a type specimen book. It has survived not only five centuries, but also the leap into electronic typesetting, remaining</p>
  <h2 class="section-title" style="top:430px">My Key Skills.</h2>
  <div class="skill" style="top:528px"><span class="skill-label">RESPONSIVE WEB DESIGN</span><div class="skill-track"><div class="skill-fill" style="width:82%"></div></div></div>
  <div class="skill" style="top:595px"><span class="skill-label">WEBSITE DEVELOPMENT</span><div class="skill-track"><div class="skill-fill" style="width:72%"></div></div></div>
  <div class="skill" style="top:660px"><span class="skill-label">INTERNET MARKETING</span><div class="skill-track"><div class="skill-fill" style="width:90%"></div></div></div>
  <div class="skill" style="top:724px"><span class="skill-label">DATA MANAGEMENT</span><div class="skill-track"><div class="skill-fill" style="width:90%"></div></div></div>
</section>

<section class="works">
  <h2 class="section-title" style="top:22px">Creative Works.</h2>
  <div class="filters"><span class="active">ALL</span><span>WEBDESIGN</span><span>DEVELOPMENT</span><span>PHOTOGRAPHY</span></div>
  <div class="work-tile" style="left:56px;top:198px;background:linear-gradient(180deg,#e6e6e6,#dcdcdc)" role="img" aria-label="Project photo: black pendant lamp on a light grey wall"></div>
  <div class="work-tile" style="left:426px;top:198px;background:linear-gradient(180deg,#ececec,#e2e2e2)" role="img" aria-label="Project image: bold black geometric letterform identity"></div>
  <div class="work-tile" style="left:796px;top:198px;background:linear-gradient(135deg,#e4e4e4,#d2d2d2)" role="img" aria-label="Project photo: printed card with leaf artwork and ampersand"></div>
  <div class="work-tile" style="left:56px;top:501px;background:linear-gradient(135deg,#e0e0e0,#cfcfcf)" role="img" aria-label="Project photo: round wall clock with black segment"></div>
  <div class="work-tile" style="left:426px;top:501px;background:linear-gradient(180deg,#ededed,#e4e4e4)" role="img" aria-label="Project image: line-drawn monogram on a grid"></div>
  <div class="work-tile" style="left:796px;top:501px;background:linear-gradient(135deg,#eeeeee,#d8d8d8)" role="img" aria-label="Project photo: embossed lettering on a white business card"></div>
</section>

<section class="blogs">
  <h2 class="section-title" style="top:26px">Recents Blogs</h2>
  <article class="post" style="left:59px">
    <div class="post-image" style="background:linear-gradient(135deg,#4a4a4a,#1c1c1c)" role="img" aria-label="Blog photo: laptop on a desk in a dark room"></div>
    <h3 class="post-title">CREATE WEBSITE STEP BY STEP</h3>
    <p class="post-text">Lorem Ipsum is simply dummy text of the printing and typesetting industry. Lorem Ipsum has been the industry.</p>
    <a class="btn post-btn" href="#">Read More</a>
  </article>
  <article class="post" style="left:426px">
    <div class="post-image" style="background:linear-gradient(135deg,#5b6650,#2b3327)" role="img" aria-label="Blog photo: tablet lying among green leaves"></div>
    <h3 class="post-title">CREATE WEBSITE STEP BY STEP</h3>
    <p class="post-text">Lorem Ipsum is simply dummy text of the printing and typesetting industry. Lorem Ipsum has been the industry.</p>
    <a class="btn post-btn" href="#">Read More</a>
  </article>
  <article class="post" style="left:793px">
    <div class="post-image" style="background:linear-gradient(135deg,#3d4349,#1b1e22)" role="img" aria-label="Blog photo: smartphone resting on dark fabric"></div>
    <h3 class="post-title">CREATE WEBSITE STEP BY STEP</h3>
    <p class="post-text">Lorem Ipsum is simply dummy text of the printing and typesetting industry. Lorem Ipsum has been the industry.</p>
    <a class="btn post-btn" href="#">Read More</a>
  </article>
</section>

<section class="freelance">
  <div class="freelance-scene" role="img" aria-label="Dark background photo of a person sitting outdoors on a pavement"></div>
  <div class="freelance-circle">I'm available for<br>freelance work</div>
  <p class="freelance-mail">hello@lanternwalk.com</p>
</section>

<section class="contact">
  <h2 class="section-title" style="top:52px">Say Hello!</h2>
  <div class="field field-line" style="top:187px">Name</div>
  <div class="field field-line" style="top:268px">Email</div>
  <div class="field field-area" style="top:351px">Your Message</div>
  <a class="btn submit" href="#">Submit Now</a>
</section>

<footer class="footer">©Copyright 2017 &nbsp;All RightReserved.</footer>

</body>
</html>
```